Crisp, Impactful, Web Design Needed

We are looking to redesign our website, beginning with our Home Page. We are a Saas company, and our product is called Kelvaro. It is an application that allows Brindlecore Development teams to more easily customize their Brindlecore Instance. In its essence, Kelvaro is a complete end-to-end DevOps solution with built-in merge tools, version control, continuous deployments, static code analysis, user story management, regression testing tools & more. Kelvaro is completely built on Brindlecore, for Brindlecore.

Our current website is www.kelvaro-example.com.

Our largest competitors are Vintera, Plumtide and NexoHalvin.

We like the simple messaging/feel that zorbeline.example utilizes.
Websites that inspire us are zorbeline.example and https://quillmora.example

Like the websites above, we want the design to be SIMPLE, CLEAN & ORGANIZED .

We are hoping the final design will incorporate our current branding, but be more clean, elegant, powerful, and drive increased action from the viewer. It should present a successful, trusted enterprise-level software image - tightly aligned with Brindlecore and communicate the overall message that we make Brindlecore development easier and save companies time, money and resources. We want to make sure we look like a large company and attract enterprise-level companies, but also connect well with Developers. Should NOT be boring, but rather crisp and impactful. I have attached the text for the homepage below as well as our logo and some of the recent materials we have put together that provide information about our company. In the text document we have provided some ideas for infographics, but hope the winning designer will use their own creativity to come up with something that will wow us. Our branding colors are Q-fennel pink - hex ea0a8e ONLY along with a grayscale/black. We do not want the final design to be too pink however - just utilizing that for statement/accent purposes.

Instead of placing the most emphasis on using cool graphics, images, etc. The focus should be on conveying the message in a clear, impactful, way. The structure of the page should be very clear. The placement should be hierarchical. The page needs to be super well-organized. See this page: [https://www.dravenholt.example/en/insights/top-insights](https://www.dravenholt.example/en/insights/top-insights)

Please place an emphasis on font/typography. The font that we must use a very easy to use font. The font should be big, clean full.

Please design multiple pages.

Please do not use any stock photos

Please do not use cartoon-like images and instead use more professional looking infographcis.

Target Market(s)

Any company that utilizes Brindlecore and customizes their Brindlecor instance, particularly enterprise-level/large organizations. Specific roles that we're looking to appeal to include CTO's, CRM Managers, Brindlecore Developers, Brindlecore Architects, Brindlecore Technical Architects, Brindlecore Program Architects

Industry/Entity Type

SaaS

Number of Pages Required

4 page

Font styles to use
Sans Serif

Colors
e664a5

Requirements
Must have
• Kelvaro Logo, \Provided Homepage Text, Graphics
Should not have
• stock photos, cartoon-like images

```html
<!DOCTYPE html>
<html lang="en">
<head>
<meta charset="utf-8">
<title>Kelvaro — Release Management for Brindlecore</title>
<link href="https://fonts.googleapis.com/css2?family=Montserrat:wght@500;600;700;800&family=Open+Sans:wght@400;600;700&display=swap" rel="stylesheet">
<style>
:root{
  --pink:#ea0a8e;
  --ink:#1c1c1c;
  --text:#444;
  --muted:#777;
  --line:#e2e2e2;
  --soft:#f1f1f1;
  --panel:#ececec;
  --dark:#222;
  --white:#fff;
}
*{box-sizing:border-box;margin:0;padding:0}
html,body{width:1200px;height:3492px;overflow:hidden}
body{font-family:"Open Sans",Arial,sans-serif;color:var(--text);background:var(--white);position:relative}
.heading{font-family:"Montserrat",Arial,sans-serif}

/* nav */
.site-nav{position:absolute;top:0;left:0;width:1200px;height:80px;background:var(--white);display:flex;align-items:center;padding:0 140px;justify-content:space-between;z-index:3}
.brand{display:flex;align-items:center;gap:12px;font-family:"Montserrat",Arial,sans-serif;font-weight:700;font-size:30px;color:var(--ink)}
.brand-dot{width:22px;height:22px;border-radius:50%;background:var(--pink)}
.nav-links{display:flex;gap:34px;list-style:none;font-size:14px;color:var(--ink);align-items:center}
.nav-links .active{background:var(--pink);color:var(--white);padding:6px 14px;border-radius:3px}

/* hero */
.hero{position:absolute;top:80px;left:0;width:1200px;height:680px}
.hero-photo{position:absolute;inset:0;background:linear-gradient(100deg,#3b3b3b 0%,#7a7773 40%,#d9d5cf 70%,#efece8 100%)}
.hero-shade{position:absolute;inset:0;background:linear-gradient(90deg,rgba(0,0,0,.55) 0%,rgba(0,0,0,.2) 50%,rgba(0,0,0,0) 70%)}
.hero-copy{position:absolute;left:70px;top:180px;color:var(--white)}
.hero-title{font-family:"Montserrat",Arial,sans-serif;font-weight:800;font-size:52px;line-height:1.05;text-transform:uppercase}
.hero-sub{font-family:"Montserrat",Arial,sans-serif;font-weight:700;font-size:17px;margin-top:14px;text-transform:uppercase}
.hero-actions{display:flex;gap:18px;margin-top:36px}
.btn{display:inline-block;font-family:"Montserrat",Arial,sans-serif;font-weight:600;font-size:15px;padding:13px 26px;border-radius:3px;text-transform:uppercase}
.btn-pink{background:var(--pink);color:var(--white)}
.btn-dark{background:rgba(20,20,20,.85);color:var(--white)}
.hero-dots{display:flex;gap:12px;margin-top:40px}
.hero-dots span{width:10px;height:10px;border-radius:50%;background:rgba(255,255,255,.5)}
.hero-dots span:first-child{background:var(--white)}

/* section headers */
.section-head{position:absolute;left:0;width:1200px;text-align:center}
.section-mark{width:34px;height:6px;background:var(--pink);margin:0 auto 16px;border-radius:3px}
.section-title{font-family:"Montserrat",Arial,sans-serif;font-weight:800;font-size:30px;color:var(--pink);text-transform:uppercase}
.section-intro{font-size:12px;color:var(--muted);width:800px;margin:14px auto 0;line-height:1.5}

/* results */
.results{position:absolute;top:975px;left:130px;width:940px;display:flex;justify-content:space-between}
.stat{width:200px;text-align:center}
.stat-ring{position:relative;width:190px;height:190px;margin:0 auto}
.stat-value{position:absolute;inset:0;display:flex;align-items:center;justify-content:center;font-family:"Montserrat",Arial,sans-serif;font-size:50px;font-weight:500;color:var(--ink)}
.stat-label{font-family:"Montserrat",Arial,sans-serif;font-weight:600;font-size:19px;color:var(--ink);margin-top:18px;line-height:1.3}
.accent-bar{position:absolute;left:140px;width:912px;height:16px;background:var(--pink)}

/* team + about */
.team-photo{position:absolute;top:1324px;left:0;width:1200px;height:400px;background:linear-gradient(180deg,#4a4a4a 0%,#6e6258 45%,#8a6a58 75%,#5a4c46 100%)}
.about-card{position:absolute;top:1680px;left:140px;width:912px;height:320px;background:var(--white);box-shadow:0 4px 18px rgba(0,0,0,.12);text-align:center;padding:36px 60px 0}
.about-card .section-mark{margin-bottom:14px}
.about-card p{font-size:12px;line-height:1.7;color:var(--muted);margin-top:16px;text-align:left}

/* solutions */
.solutions{position:absolute;top:2188px;left:180px;width:840px;display:flex;justify-content:space-between}
.solution{width:400px;height:244px;text-align:center;padding-top:20px}
.solution-outline{border:2px solid var(--ink)}
.solution-name{font-family:"Montserrat",Arial,sans-serif;font-weight:700;font-size:15px;color:var(--ink);margin-top:12px;text-transform:uppercase}
.solution-desc{font-size:11px;color:var(--muted);line-height:1.45;width:300px;margin:8px auto 0}

/* cta */
.cta-frame{position:absolute;top:2540px;left:260px;width:680px;height:370px;background:#cfcfcf;border-radius:20px 20px 0 0;padding:16px 16px 0}
.cta-screen{width:100%;height:100%;background:var(--dark);border-radius:8px 8px 0 0;text-align:center;padding-top:80px;color:var(--white)}
.cta-title{font-family:"Montserrat",Arial,sans-serif;font-weight:600;font-size:40px;line-height:1.2}
.cta-screen .btn{margin-top:30px;background:var(--dark);border:2px solid var(--white);font-size:13px;padding:10px 24px}

/* partners */
.partners{position:absolute;top:2900px;left:0;width:1200px;height:260px;background:var(--soft);text-align:center}
.partner-tabs{display:flex;justify-content:center;gap:70px;padding-top:48px}
.partner-tab{width:440px;height:52px;border-radius:26px;background:var(--white);border:1px solid var(--line);display:flex;align-items:center;justify-content:center;font-family:"Montserrat",Arial,sans-serif;font-weight:700;font-size:15px;color:var(--ink);text-transform:uppercase}
.partner-tab.current{color:var(--pink)}
.partner-note{font-size:12px;color:var(--muted);margin-top:26px}
.partner-row{display:flex;justify-content:center;gap:110px;margin-top:26px;font-family:"Montserrat",Arial,sans-serif;font-weight:600;font-size:24px;color:#9a9a9a}

/* footer */
.site-footer{position:absolute;top:3160px;left:0;width:1200px;height:300px;background:var(--panel);display:flex;padding:40px 140px 0;gap:60px}
.footer-col{flex:1}
.footer-col:first-child{flex:1.1}
.footer-col .brand{font-size:28px}
.footer-blurb{font-size:11px;color:var(--muted);line-height:1.6;margin-top:12px;width:190px}
.footer-title{font-family:"Montserrat",Arial,sans-serif;font-weight:800;font-size:18px;color:var(--ink);text-transform:uppercase;border-bottom:3px solid var(--pink);display:inline-block;padding-bottom:4px}
.footer-links{list-style:none;margin-top:16px;font-size:12px;color:var(--text)}
.footer-links li{margin-bottom:9px}
.footer-links li::before{content:"›";color:var(--pink);margin-right:10px;font-weight:700}
.field{width:220px;height:30px;background:var(--ink);margin-top:14px}
.field + .field{margin-top:10px}
.signup{display:inline-block;background:var(--pink);color:var(--white);font-size:11px;font-weight:700;padding:7px 20px;margin-top:12px}
.contact-line{display:flex;align-items:center;gap:10px;font-size:12px;margin-top:16px}
.copyright{position:absolute;top:3460px;left:0;width:1200px;height:32px;background:var(--dark);color:#aaa;font-size:11px;text-align:center;line-height:32px}
</style>
</head>
<body>

<nav class="site-nav">
  <div class="brand"><span class="brand-dot"></span>Kelvaro</div>
  <ul class="nav-links">
    <li class="active">Home</li>
    <li>About Kelvaro</li>
    <li>Kelvaro Solutions</li>
    <li>Customers</li>
    <li>Partners ▾</li>
    <li>Contact</li>
  </ul>
</nav>

<header class="hero">
  <div class="hero-photo" role="img" aria-label="Photo of a smiling professional in glasses holding a tablet in a bright office"></div>
  <div class="hero-shade"></div>
  <div class="hero-copy">
    <h1 class="hero-title">Discover<br>Life-Changing<br>Release Management</h1>
    <p class="hero-sub">Unlock a worry-free workflow with the power of native releases</p>
    <div class="hero-actions">
      <span class="btn btn-pink">Learn More</span>
      <span class="btn btn-dark">Request Demo</span>
    </div>
    <div class="hero-dots"><span></span><span></span><span></span></div>
  </div>
</header>

<section class="section-head" style="top:826px">
  <div class="section-mark"></div>
  <h2 class="section-title">Our Results</h2>
  <p class="section-intro">Our results speak for themselves. Kelvaro has shown to provably lower the total cost of ownership, increase developer efficiency, deliver more features and reduce compliance costs.</p>
</section>

<div class="results">
  <div class="stat">
    <div class="stat-ring">
      <svg width="190" height="190" viewBox="0 0 190 190"><circle cx="95" cy="95" r="85" fill="none" stroke="var(--line)" stroke-width="3"/><circle cx="95" cy="95" r="85" fill="none" stroke="var(--pink)" stroke-width="9" stroke-dasharray="171 534" transform="rotate(-90 95 95)"/></svg>
      <div class="stat-value">32%</div>
    </div>
    <p class="stat-label">Lower cost of<br>ownership</p>
  </div>
  <div class="stat">
    <div class="stat-ring">
      <svg width="190" height="190" viewBox="0 0 190 190"><circle cx="95" cy="95" r="85" fill="none" stroke="var(--line)" stroke-width="3"/><circle cx="95" cy="95" r="85" fill="none" stroke="var(--pink)" stroke-width="9" stroke-dasharray="155 534" transform="rotate(-90 95 95)"/></svg>
      <div class="stat-value">29%</div>
    </div>
    <p class="stat-label">Increase in<br>developer efficiency</p>
  </div>
  <div class="stat">
    <div class="stat-ring">
      <svg width="190" height="190" viewBox="0 0 190 190"><circle cx="95" cy="95" r="85" fill="none" stroke="var(--line)" stroke-width="3"/><circle cx="95" cy="95" r="85" fill="none" stroke="var(--pink)" stroke-width="9" stroke-dasharray="219 534" transform="rotate(-90 95 95)"/></svg>
      <div class="stat-value">41%</div>
    </div>
    <p class="stat-label">More features<br>delivered</p>
  </div>
  <div class="stat">
    <div class="stat-ring">
      <svg width="190" height="190" viewBox="0 0 190 190"><circle cx="95" cy="95" r="85" fill="none" stroke="var(--line)" stroke-width="3"/><circle cx="95" cy="95" r="85" fill="none" stroke="var(--pink)" stroke-width="9" stroke-dasharray="288 534" transform="rotate(-90 95 95)"/></svg>
      <div class="stat-value">54%</div>
    </div>
    <p class="stat-label">Reduction of<br>compliance costs</p>
  </div>
</div>

<div class="accent-bar" style="top:1308px"></div>

<div class="team-photo" role="img" aria-label="Photo of a cheerful diverse team standing together in front of a dark wall"></div>

<section class="about-card">
  <div class="section-mark"></div>
  <h2 class="section-title">About Our Company</h2>
  <p>Kelvaro is an international software company that has pioneered the Brindlecore application life cycle development sector. Our firm is focused on transforming the DevOps experience for our clients, allowing them to accelerate their operational agility and improve collaboration. The unique architecture of our products provides security, governance and compliance abilities that are unmatched in the industry. We are trusted by some of the largest brands around the world and provide a standard team for tools, training and knowledge transfer to each of our customers who operate in a multitude of industries.</p>
</section>
<div class="accent-bar" style="top:1996px"></div>

<section class="section-head" style="top:2104px">
  <div class="section-mark"></div>
  <h2 class="section-title">Kelvaro Solutions</h2>
</section>

<div class="solutions">
  <article class="solution">
    <svg width="90" height="80" viewBox="0 0 90 80" aria-hidden="true">
      <path d="M22 44a14 14 0 0 1 2-28 20 20 0 0 1 38-2 15 15 0 0 1 6 30z" fill="var(--pink)"/>
      <g stroke="var(--ink)" stroke-width="2" fill="none">
        <line x1="45" y1="44" x2="45" y2="72"/><line x1="33" y1="44" x2="25" y2="66"/><line x1="57" y1="44" x2="65" y2="66"/>
      </g>
      <circle cx="45" cy="74" r="3" fill="var(--ink)"/><circle cx="24" cy="68" r="3" fill="var(--ink)"/><circle cx="66" cy="68" r="3" fill="var(--ink)"/>
    </svg>
    <h3 class="solution-name">DevOps &amp; Release Management</h3>
    <p class="solution-desc">Kelvaro is a true end-to-end native Brindlecore application lifecycle management solution. It provides version control, continuous integration, conflict management, regression testing and more.</p>
  </article>
  <article class="solution solution-outline">
    <svg width="90" height="80" viewBox="0 0 90 80" aria-hidden="true">
      <circle cx="45" cy="40" r="38" fill="var(--ink)"/>
      <g fill="var(--white)">
        <ellipse cx="50" cy="26" rx="16" ry="5"/>
        <rect x="34" y="30" width="32" height="10" rx="3"/>
        <rect x="34" y="43" width="32" height="10" rx="3"/>
        <rect x="34" y="56" width="32" height="8" rx="3"/>
      </g>
      <path d="M14 30h12l-4-4M26 30l-4 4" stroke="var(--pink)" stroke-width="3" fill="none"/>
    </svg>
    <h3 class="solution-name">Data Migration</h3>
    <p class="solution-desc">Kelvaro Data Migration tool allows developers to easily move records between environments, keeping related data intact across all orgs.</p>
  </article>
</div>

<section class="cta-frame">
  <div class="cta-screen">
    <h2 class="cta-title">Ready to simplify your<br>Brindlecore Deployment?</h2>
    <span class="btn">Book Demo</span>
  </div>
</section>

<section class="partners">
  <div class="partner-tabs">
    <div class="partner-tab current">Technology Partners</div>
    <div class="partner-tab">Enterprise Implementation Partners</div>
  </div>
  <p class="partner-note">Kelvaro partners with multiple technology firms to bring best in class release management opportunities.</p>
  <div class="partner-row">
    <span>Norvane</span><span>Velmora</span><span>Aptrelle</span><span>Brindlecore</span><span>Vantrix</span>
  </div>
</section>

<footer class="site-footer">
  <div class="footer-col">
    <div class="brand"><span class="brand-dot"></span>Kelvaro</div>
    <p class="footer-blurb">Kelvaro is an international software company that has pioneered the Brindlecore application life cycle development sector.</p>
  </div>
  <div class="footer-col">
    <h4 class="footer-title">Quick Links</h4>
    <ul class="footer-links">
      <li>Home</li><li>About Kelvaro</li><li>Kelvaro Solutions</li><li>Customers</li><li>Partners</li><li>Contact</li>
    </ul>
  </div>
  <div class="footer-col">
    <h4 class="footer-title">Newsletter</h4>
    <div class="field"></div>
    <div class="field"></div>
    <span class="signup">SIGN UP</span>
  </div>
  <div class="footer-col">
    <h4 class="footer-title">Contact Us</h4>
    <p class="contact-line">
      <svg width="16" height="12" viewBox="0 0 16 12" aria-hidden="true"><rect x="0.5" y="0.5" width="15" height="11" fill="none" stroke="var(--pink)"/><path d="M1 1l7 6 7-6" fill="none" stroke="var(--pink)"/></svg>
      info@kelvaro-example.com</p>
    <p class="contact-line">
      <svg width="14" height="14" viewBox="0 0 14 14" aria-hidden="true"><path d="M3 1l3 3-2 2a8 8 0 0 0 4 4l2-2 3 3-2 2C6 13 1 8 1 3z" fill="var(--pink)"/></svg>
      (555) 010-4420</p>
  </div>
</footer>
<div class="copyright">©2024 Kelvaro Inc. All rights reserved.</div>

</body>
</html>
```